Business Card Design Project

We need a business card to reflect the design of our website - just so it all ties in - it has a retro feel and can be found at http://www.velorasoulpair.com
We will need our phone 0437 215 964
Web address, and email velorapair@fernmail.com included
Our catch cry is "Classic Cocktail Music"
Perfect Live Music for Private & Corporate Events, Weddings and Dinner Music
Our names should be included :-
Maribel Thorne / piano & Dennis Holloway / bass
I am now also including our logo so that it can be included (in part or whole) somehow in the design
My partner thinks we should include our logo in some form in the design of the card - i will attach this here for you. I will attach eps but if you prefer another format please let me know
Regards
Mari

```html
<!DOCTYPE html>
<html lang="en">
<head>
<meta charset="utf-8">
<title>Velora Pair – Business Cards</title>
<link rel="stylesheet" href="https://fonts.googleapis.com/css2?family=Righteous&family=Didact+Gothic&family=Poiret+One&display=swap">
<style>
  :root{
    --page:#f7f9fa;
    --teal:#74a9a9;
    --teal-dark:#679a9a;
    --teal-text:#6fa8a8;
    --cream:#efe5ca;
    --cream-dark:#e6d9b8;
    --coral:#e7785e;
    --coral-dark:#d96b52;
    --charcoal:#484848;
    --ink:#3d3d3d;
    --shadow:rgba(0,0,0,.18);
  }
  *{box-sizing:border-box;margin:0;padding:0}
  html,body{width:1200px;height:946px;overflow:hidden;background:var(--page)}
  .sheet{position:relative;width:1200px;height:946px}
  .card{position:absolute;width:251px;height:391px;border-radius:3px;overflow:hidden;box-shadow:0 1px 4px var(--shadow)}
  .card--front{background:linear-gradient(180deg,var(--teal) 0%,var(--teal-dark) 100%)}
  .card--back{background:linear-gradient(160deg,#f2e9d2 0%,var(--cream) 60%,var(--cream-dark) 100%)}

  /* front */
  .front-cap{position:absolute;left:0;top:0;width:251px;height:68px;border-bottom:1px dashed rgba(255,255,255,.35)}
  .front-cap--teal{background:linear-gradient(180deg,#7fb6b6,var(--teal))}
  .front-cap--cream{background:var(--cream)}
  .seal-ring{position:absolute;left:78px;top:-4px;width:96px;height:96px;border-radius:50%;border:1px dashed rgba(255,255,255,.4)}
  .front-cap--teal + .seal-ring{background:var(--teal)}
  .front-cap--cream + .seal-ring{background:var(--cream);border-color:rgba(90,90,90,.35)}
  .seal{position:absolute;left:84px;top:2px;width:84px;height:84px;border-radius:50%;background:var(--charcoal);
        display:flex;align-items:center;justify-content:center;text-align:center;
        font-family:"Didact Gothic",sans-serif;font-size:12px;line-height:1.15;color:var(--cream);letter-spacing:1px}
  .front-title{position:absolute;left:0;width:251px;top:180px;text-align:center;
        font-family:"Poiret One",sans-serif;font-size:30px;color:#5c7d75;letter-spacing:1px}
  .front-tagline{position:absolute;left:0;width:251px;top:220px;text-align:center;
        font-family:"Didact Gothic",sans-serif;font-size:8.5px;color:var(--ink)}
  .coral-band{position:absolute;left:0;bottom:0;width:251px;height:33px;
        background:linear-gradient(180deg,var(--coral),var(--coral-dark));
        font-family:"Didact Gothic",sans-serif;font-size:8.5px;color:var(--ink);text-align:center;line-height:38px}
  .coral-band::before{content:"";position:absolute;left:0;right:0;top:5px;border-top:1px dashed rgba(255,255,255,.35)}

  /* back */
  .side-strip{position:absolute;left:0;top:0;width:10px;height:100%;background:var(--teal);border-right:1px solid rgba(0,0,0,.08)}
  .badge{position:absolute;right:16px;top:2px;width:44px;height:48px}
  .badge-name{position:absolute;right:23px;top:12px;width:30px;height:30px;border-radius:50%;background:var(--charcoal);
        display:flex;align-items:center;justify-content:center;text-align:center;
        font-family:"Didact Gothic",sans-serif;font-size:6px;line-height:1.1;color:var(--cream)}
  .motto{position:absolute;left:10px;width:241px;text-align:center;font-family:"Righteous",sans-serif;
        font-size:13px;color:var(--teal-text);letter-spacing:.3px}
  .back-tagline{position:absolute;left:10px;width:241px;top:123px;text-align:center;
        font-family:"Didact Gothic",sans-serif;font-size:8.5px;color:var(--ink)}
  .member{position:absolute;right:21px;text-align:right;font-family:"Didact Gothic",sans-serif}
  .member-name{font-size:13.5px;letter-spacing:1.6px;color:var(--teal-text);line-height:1}
  .member-role{font-size:10.5px;letter-spacing:1.4px;color:var(--coral);font-style:italic;line-height:1.05}
  .contacts{position:absolute;left:20px;top:298px;list-style:none;font-family:"Didact Gothic",sans-serif;font-size:5px;letter-spacing:.9px;color:var(--ink)}
  .contacts li{display:flex;align-items:center;height:12.5px}
  .contacts svg{width:10px;height:10px;margin-right:11px;fill:#222}
</style>
</head>
<body>
<main class="sheet">

  <!-- row 1 -->
  <section class="card card--front" style="left:312px;top:50px">
    <div class="front-cap front-cap--teal"></div>
    <div class="seal-ring"></div>
    <div class="seal">Velora<br>Pair</div>
    <h1 class="front-title">VELORA PAIR</h1>
    <p class="front-tagline">weddings, corporate and private events, dinner music</p>
    <footer class="coral-band">www.velorasoulpair.com</footer>
  </section>

  <section class="card card--back" style="left:632px;top:50px">
    <div class="side-strip"></div>
    <svg class="badge" viewBox="0 0 44 48"><path d="M0 0H44V36Q22 52 0 36Z" fill="var(--teal)"/></svg>
    <div class="badge-name">Velora<br>Pair</div>
    <h2 class="motto" style="top:98px">CLASSIC COCKTAIL MUSIC</h2>
    <div class="member" style="top:205px"><div class="member-name">Maribel Thorne</div><div class="member-role">piano</div></div>
    <div class="member" style="top:248px"><div class="member-name">Dennis Holloway</div><div class="member-role">bass</div></div>
    <ul class="contacts">
      <li><svg viewBox="0 0 10 10"><path d="M5 0L10 5H8.5V10H6V7H4V10H1.5V5H0Z"/></svg>14/52 Harlow Street Ashgrove Queensland 4060 · Australia</li>
      <li><svg viewBox="0 0 10 10"><path d="M2 0L4 2.5 3 4Q4.5 6.5 6 7L7.5 6 10 8 8 10Q1 8 0 2Z"/></svg>0437 215 964</li>
      <li><svg viewBox="0 0 10 10"><rect x="1.5" y="1" width="7" height="8"/></svg>velorapair@fernmail.com</li>
      <li><svg viewBox="0 0 10 10"><path d="M0 4L5 0 10 4V10H0Z M1 4.5L5 7.5 9 4.5" stroke="#efe5ca" stroke-width=".8"/></svg>www.velorasoulpair.com</li>
    </ul>
    <footer class="coral-band">weddings, corporate and private events, dinner music</footer>
  </section>

  <!-- row 2 -->
  <section class="card card--front" style="left:312px;top:473px">
    <div class="front-cap front-cap--cream"></div>
    <div class="seal-ring"></div>
    <div class="seal">Velora<br>Pair</div>
    <h1 class="front-title">VELORA PAIR</h1>
    <footer class="coral-band">www.velorasoulpair.com</footer>
  </section>

  <section class="card card--back" style="left:632px;top:473px">
    <div class="side-strip"></div>
    <svg class="badge" viewBox="0 0 44 48"><path d="M0 0H44V36Q22 52 0 36Z" fill="var(--teal)"/></svg>
    <div class="badge-name">Velora<br>Pair</div>
    <h2 class="motto" style="top:98px">CLASSIC COCKTAIL MUSIC</h2>
    <p class="back-tagline">weddings, corporate and private events, dinner music</p>
    <div class="member" style="top:205px"><div class="member-name">Maribel Thorne</div><div class="member-role">piano</div></div>
    <div class="member" style="top:248px"><div class="member-name">Dennis Holloway</div><div class="member-role">bass</div></div>
    <ul class="contacts">
      <li><svg viewBox="0 0 10 10"><path d="M5 0L10 5H8.5V10H6V7H4V10H1.5V5H0Z"/></svg>14/52 Harlow Street Ashgrove Queensland 4060 · Australia</li>
      <li><svg viewBox="0 0 10 10"><path d="M2 0L4 2.5 3 4Q4.5 6.5 6 7L7.5 6 10 8 8 10Q1 8 0 2Z"/></svg>0437 215 964</li>
      <li><svg viewBox="0 0 10 10"><rect x="1.5" y="1" width="7" height="8"/></svg>velorapair@fernmail.com</li>
      <li><svg viewBox="0 0 10 10"><path d="M0 4L5 0 10 4V10H0Z M1 4.5L5 7.5 9 4.5" stroke="#efe5ca" stroke-width=".8"/></svg>www.velorasoulpair.com</li>
    </ul>
    <footer class="coral-band"></footer>
  </section>

</main>
</body>
</html>
```